Piano genealogy graphs template, for a large poster printing

Hello and thank you for your interest in my project.
I need a poster template, so I can create structures similar to the one I have uploaded. I want to completely replace or improve my poor previous design which is attached.
I need to be able to input names and dates into boxes of various colors, arrows pointing between boxes. I would also like to be able to label each graph (not each box).
I am looking at something that would be legible when printed, in a one consistent professional layout of 2A0 (around 1189x1682 mm) poster (I know it is large). The design template required here can include just few sample text boxes with sample flags on a suitable background, for me to multiply later and spread across the whole poster.
The positioning of the boxes is not important.
Please let me know if more clarification is required.
Thank you for your help.

Feel free to follow what I have attached in the file, or change the design completely.

UPDATE 4/12: I have uploaded two more graphs as an example. At this stage of the contest, I would like to have one of those graphs done, and I am planning to offer a 'freelance job' to one or two designers, who will be willing to do the whole 10 graphs on one poster.
Updates

Reason: Dear Designers, Since the project is rather complex and large-scale, I have decided to give everyone more time to work on their designs. I will consider extending it further if any of you require additional time. Best wishes, bronisław

Dear Designers, I would like to inform you that the contest for my poster is now closed and that I have assigned the prizes. I would like to thank all of you for submiting your high-quality designs, and for your participation. It was a great pleasure working with all of you. Due to the large size of the project itself (large number of graphs to be fitted on a single poster), I had to focus on providing feedback to only those designers who provided projects closest to what I was expecting at the early stages of the contest. I wish you all the best for the future, Kind regards, Bronisław

Target Market(s)

Pianists, historians

Industry/Entity Type

Printing

Requirements
Must have
• Consistent design, but allow to clearly delineate various genealogy trees.

```html
<!DOCTYPE html>
<html lang="en">
<head>
<meta charset="utf-8">
<title>Genealogical Trees of Pianists — French Tree, Branch I</title>
<link rel="stylesheet" href="https://fonts.googleapis.com/css2?family=Poiret+One&family=Advent+Pro:wght@400;500&display=swap">
<style>
  :root {
    --paper-light: #fffaf4;
    --paper-mid: #f6e9de;
    --paper-edge: #ead5c6;
    --ink: #4a1c1a;
    --band: #f7e5db;
    --box-dark: #4a1410;
    --box-light: #bb7a6c;
    --box-text: #fbf0ea;
    --arrow: #5a2320;
  }
  html, body {
    margin: 0;
    padding: 0;
    overflow: hidden;
  }
  .poster {
    position: relative;
    width: 848px;
    height: 1200px;
    overflow: hidden;
  }
  .poster__background {
    position: absolute;
    inset: 0;
    background: radial-gradient(ellipse 75% 60% at 50% 52%, var(--paper-light) 0%, var(--paper-mid) 70%, var(--paper-edge) 100%);
  }
  .poster__title {
    position: absolute;
    left: 68px;
    top: 38px;
    margin: 0;
    font-family: "Poiret One", sans-serif;
    font-weight: 400;
    font-size: 60px;
    letter-spacing: 0;
    line-height: 1;
    color: var(--ink);
    white-space: nowrap;
    transform: scaleX(0.7);
    transform-origin: left top;
  }
  .tree-label {
    position: absolute;
    left: 47px;
    top: 154px;
    width: 417px;
    height: 49px;
    background: var(--band);
    margin: 0;
    padding-left: 9px;
    box-sizing: border-box;
    font-family: "Advent Pro", sans-serif;
    font-weight: 500;
    font-size: 42px;
    line-height: 49px;
    color: var(--ink);
    white-space: nowrap;
  }
  .person-box {
    position: absolute;
    box-sizing: border-box;
    margin: 0;
    padding: 10px 10px 0 16px;
    background: linear-gradient(to bottom, var(--box-dark) 0%, var(--box-light) 50%, var(--box-dark) 100%);
    color: var(--box-text);
    font-family: "Poiret One", sans-serif;
    font-size: 14px;
    font-weight: 400;
    line-height: 17.6px;
    white-space: nowrap;
    overflow: hidden;
  }
  .person-box--small { width: 290px; height: 131px; }
  .person-box--large {
    width: 289px;
    height: 218px;
    padding-top: 18px;
    font-family: "Advent Pro", sans-serif;
    font-size: 22px;
    line-height: 29.6px;
  }
  .person-box--large .person-box__lines {
    display: block;
    transform: scaleX(0.6);
    transform-origin: left top;
  }
  .box-1 { left: 49px; top: 242px; }
  .box-2 { left: 526px; top: 242px; }
  .box-3 { left: 49px; top: 544px; }
  .box-4 { left: 526px; top: 457px; }
  .arrow {
    position: absolute;
    overflow: visible;
  }
  .arrow path, .arrow polygon { fill: var(--arrow); }
  .arrow line { stroke: var(--arrow); stroke-width: 3; }
  .arrow--right { width: 154px; height: 30px; left: 353px; }
  .arrow--right-1 { top: 297px; }
  .arrow--right-2 { top: 583px; }
  .arrow--down { width: 30px; height: 156px; left: 151px; top: 379px; }
</style>
</head>
<body>
<main class="poster">
  <div class="poster__background" role="img" aria-label="Cream paper background with a faint pale floral leaf pattern"></div>

  <h1 class="poster__title">GENEALOGICAL TREES OF PIANISTS</h1>
  <h2 class="tree-label">FRENCH TREE, BRANCH I</h2>

  <p class="person-box person-box--small box-1">Lorem ipsum dolor sit amet, consectetur<br>adipisicing elit, sed do eiusmod tempor<br>incididunt ut labore et dolore magna aliqua.<br>Ut enim ad minim veniam, quis nostrud<br>exercitation ullamco laboris nisi ut aliquip<br>ex ea commodo modi tempora incidunt ut</p>

  <svg class="arrow arrow--right arrow--right-1" viewBox="0 0 154 30" aria-hidden="true">
    <line x1="14" y1="15" x2="140" y2="15"/>
    <path d="M0 7 H22 L30 15 L22 23 H0 L8 15 Z"/>
    <polygon points="154,15 128,3 134,15 128,27"/>
  </svg>

  <p class="person-box person-box--small box-2">Lorem ipsum dolor sit amet, consectetur<br>adipisicing elit, sed do eiusmod tempor<br>incididunt ut labore et dolore magna aliqua.<br>Ut enim ad minim veniam, quis nostrud<br>exercitation ullamco laboris nisi ut aliquip<br>ex ea commodo modi tempora incidunt ut</p>

  <svg class="arrow arrow--down" viewBox="0 0 30 156" aria-hidden="true">
    <line x1="15" y1="14" x2="15" y2="142"/>
    <path d="M4 0 L15 12 L26 0 V22 L15 32 L4 22 Z"/>
    <polygon points="15,156 3,128 15,134 27,128"/>
  </svg>

  <p class="person-box person-box--small box-3">Lorem ipsum dolor sit amet, consectetur<br>adipisicing elit, sed do eiusmod tempor<br>incididunt ut labore et dolore magna aliqua.<br>Ut enim ad minim veniam, quis nostrud<br>exercitation ullamco laboris nisi ut aliquip<br>ex ea commodo modi tempora incidunt ut</p>

  <svg class="arrow arrow--right arrow--right-2" viewBox="0 0 154 30" aria-hidden="true">
    <line x1="14" y1="15" x2="140" y2="15"/>
    <path d="M0 7 H22 L30 15 L22 23 H0 L8 15 Z"/>
    <polygon points="154,15 128,3 134,15 128,27"/>
  </svg>

  <p class="person-box person-box--large box-4"><span class="person-box__lines">Lorem ipsum dolor sit amet, consectetur<br>adipisicing elit, sed do eiusmod tempor<br>incididunt ut labore et dolore magna aliqua.<br>Ut enim ad minim veniam, quis nostrud<br>exercitation ullamco laboris nisi ut aliquip<br>ex ea commodo modi tempora incidunt ut</span></p>
</main>
</body>
</html>
```